20 years old IT solutions company needs brand new corporate style.

We are based in Latvia. Our business is ERP systems implementation, IT infrastructure building and supporting our customers. We are moving from traditional Add-hoc projects model to standardized flat-rate offerings. Our technology platform is Quorvanel. The value proposition of our offerings is based around simplicity, transparency, quality, peace of mind, trust, easy of doing business.
We have created the new logo and now we expect to have full stationary with both color palette and fonts which must be unicode (to ensure proper Latvian language characters display)

Target Market(s)

Small and Medium Enterprise

Requirements
Must have
• Would like to to see not only B&W but colored versions as well.

```html
<!DOCTYPE html>
<html lang="en">
<head>
<meta charset="utf-8">
<title>Lindera Tech — Stationery Set</title>
<link rel="stylesheet" href="https://fonts.googleapis.com/css2?family=Barlow+Semi+Condensed:wght@300;400&family=Lato:wght@400;700;900&display=swap">
<style>
  :root {
    --backdrop: #d9e4ef;
    --paper: #ffffff;
    --brand-blue: #2ca1dc;
    --ink-grey: #5c5f66;
    --rule-grey: #9a9ca2;
    --shadow: 0 2px 8px rgba(60, 80, 110, 0.28);
  }
  * { box-sizing: border-box; margin: 0; padding: 0; }
  html, body { width: 1200px; height: 831px; overflow: hidden; }
  body { background: var(--backdrop); position: relative; font-family: "Lato", sans-serif; color: var(--ink-grey); }

  .sheet { position: absolute; background: var(--paper); box-shadow: var(--shadow); overflow: hidden; }
  .footer-wave { position: absolute; left: 0; bottom: 0; width: 100%; display: block; }

  /* Brand name lockup */
  .brand { position: absolute; display: flex; align-items: center; gap: 6px; }
  .brand-square { border: 2px solid var(--brand-blue); flex: none; }
  .brand-name { font-family: "Lato", sans-serif; font-weight: 900; color: var(--brand-blue); letter-spacing: 0.06em; line-height: 1.05; text-transform: uppercase; }
  .brand.on-blue .brand-square { border-color: #fff; }
  .brand.on-blue .brand-name { color: #fff; }

  /* Contact blocks */
  .contact { position: absolute; font-family: "Lato", sans-serif; color: var(--ink-grey); }
  .contact p { white-space: nowrap; }
  .contact .row { display: flex; align-items: center; gap: 5px; }
  .contact svg { flex: none; fill: var(--brand-blue); }

  /* Letterhead */
  .letterhead { left: 117px; top: 111px; width: 430px; height: 609px; }
  .letterhead .brand { left: 40px; top: 44px; }
  .letterhead .brand-square { width: 40px; height: 46px; }
  .letterhead .brand-name { font-size: 13px; }
  .letterhead .contact { right: 41px; top: 38px; font-size: 7.6px; line-height: 9.6px; text-align: right; }
  .letterhead .contact .row { justify-content: flex-end; margin-top: 1.4px; }
  .letterhead .contact .gap { height: 4.5px; }
  .letter-body { position: absolute; left: 40px; top: 199px; width: 349px; font-family: "Barlow Semi Condensed", sans-serif; font-weight: 300; font-size: 9.4px; line-height: 15px; color: #4a4d54; }
  .letter-body p { margin-bottom: 15px; text-align: justify; }
  .letter-body .salutation { margin-bottom: 13px; }
  .letter-body .closing { margin-top: 32px; margin-bottom: 4px; }
  .signature { width: 36px; height: 24px; border-radius: 3px; background: linear-gradient(90deg, rgba(44,161,220,0.22), rgba(44,161,220,0.08)); }

  /* Business cards */
  .card-front { left: 635px; top: 112px; width: 183px; height: 104px; }
  .card-front .brand { left: 26px; top: 36px; gap: 4px; }
  .card-front .brand-square { width: 22px; height: 34px; }
  .card-front .brand-name { font-size: 7.4px; }
  .card-front .divider { position: absolute; left: 88px; top: 27px; width: 0.6px; height: 52px; background: #c9cbd0; }
  .card-front .holder { position: absolute; left: 100px; top: 23px; }
  .card-front .holder-name { font-weight: 700; font-size: 8.2px; color: var(--brand-blue); line-height: 10px; }
  .card-front .holder-role { font-size: 4.5px; color: var(--ink-grey); }
  .card-front .contact { left: 100px; top: 46px; font-size: 4.2px; line-height: 5.6px; }
  .card-front .contact .gap { height: 2.2px; }
  .card-front .contact .row { gap: 3px; margin-top: 0.9px; }

  .card-back { left: 904px; top: 111px; width: 182px; height: 104px; background: var(--brand-blue); }
  .card-back .brand { left: 47px; top: 35px; gap: 4px; }
  .card-back .brand-square { width: 20px; height: 34px; }
  .card-back .brand-name { font-size: 8px; }

  /* Envelopes */
  .envelope-back { left: 635px; top: 248px; width: 451px; height: 226px; }
  .envelope-back .flap { position: absolute; left: 0; top: 0; display: block; }
  .envelope-back .brand { left: 212px; top: 18px; gap: 3px; }
  .envelope-back .brand-square { width: 11px; height: 28px; }
  .envelope-back .brand-name { font-size: 6.2px; }

  .envelope-front { left: 635px; top: 494px; width: 451px; height: 226px; }
  .envelope-front .brand { left: 42px; top: 33px; }
  .envelope-front .brand-square { width: 40px; height: 50px; }
  .envelope-front .brand-name { font-size: 13px; }
  .envelope-front .contact { left: 42px; top: 143px; font-size: 7px; line-height: 9px; }
  .envelope-front .contact .gap { height: 3px; }
  .envelope-front .contact .row { margin-top: 0.6px; }
</style>
</head>
<body>

<!-- Letterhead -->
<section class="sheet letterhead" aria-label="Letterhead">
  <div class="brand">
    <span class="brand-square"></span>
    <span class="brand-name">Lindera<br>Tech</span>
  </div>

  <div class="contact">
    <p>1234 First Line Address</p>
    <p>5678 Second Line Address</p>
    <div class="gap"></div>
    <p class="row">(777) 888-7777 <svg width="7" height="7" viewBox="0 0 24 24"><path d="M6.6 10.8a15.1 15.1 0 0 0 6.6 6.6l2.2-2.2a1 1 0 0 1 1-.25 11.4 11.4 0 0 0 3.6.57 1 1 0 0 1 1 1V20a1 1 0 0 1-1 1A17 17 0 0 1 3 4a1 1 0 0 1 1-1h3.5a1 1 0 0 1 1 1c0 1.25.2 2.45.57 3.57a1 1 0 0 1-.25 1z"/></svg></p>
    <p class="row">info@yourmail.com <svg width="7" height="7" viewBox="0 0 24 24"><path d="M2 5h20v14H2z M3 6l9 7 9-7" stroke="#fff" stroke-width="1.5"/></svg></p>
    <p class="row">www.yourwebsite.com <svg width="7" height="7" viewBox="0 0 24 24"><circle cx="12" cy="12" r="10"/><path d="M2 12h20M12 2c3 3 3 17 0 20M12 2c-3 3-3 17 0 20" stroke="#fff" stroke-width="1.3" fill="none"/></svg></p>
  </div>

  <div class="letter-body">
    <p class="salutation">Dear Sir/Mam,</p>
    <p>Contrary to popular belief, Lorem Ipsum is not simply random text. It has roots in a piece of classical Latin literature from 45 BC, making it over 2000 years old. Edwin Marlowe, a Latin professor at Ashgrove College in Virginia, looked up one of the more obscure Latin words, consectetur.</p>
    <p>Lorem Ipsum comes from sections 1.10.32 and 1.10.33 of "de Finibus Bonorum et Malorum" (The Extremes of Good and Evil) by Varrenus, written in 45 BC. This book is a treatise on the theory of ethics, very popular during the Renaissance. The first line of Lorem Ipsum.</p>
    <p>The standard chunk of Lorem Ipsum used since the 1500s is reproduced below for those interested. Sections 1.10.32 and 1.10.33 from "de Finibus Bonorum et Malorum" by Varrenus are also reproduced in their exact original.</p>
    <p>The standard chunk of Lorem Ipsum used since the 1500s is reproduced below for those interested.</p>
    <p class="closing">Best Regards</p>
    <div class="signature" role="img" aria-label="Handwritten signature"></div>
  </div>

  <svg class="footer-wave" width="430" height="28" viewBox="0 0 430 28" preserveAspectRatio="none">
    <path d="M0 11 Q215 -8 430 11" stroke="var(--rule-grey)" stroke-width="1.6" fill="none"/>
    <path d="M0 16 Q215 1 430 16 V28 H0Z" fill="var(--brand-blue)"/>
  </svg>
</section>

<!-- Business card front -->
<section class="sheet card-front" aria-label="Business card front">
  <div class="brand">
    <span class="brand-square"></span>
    <span class="brand-name">Lindera<br>Tech</span>
  </div>
  <span class="divider"></span>
  <div class="holder">
    <p class="holder-name">JOHN SMITH</p>
    <p class="holder-role">Founder &amp; CEO</p>
  </div>
  <div class="contact">
    <p>1234 First Line Address</p>
    <p>5678 Second Line Address</p>
    <div class="gap"></div>
    <p class="row"><svg width="4" height="4" viewBox="0 0 24 24"><path d="M6.6 10.8a15.1 15.1 0 0 0 6.6 6.6l2.2-2.2a1 1 0 0 1 1-.25 11.4 11.4 0 0 0 3.6.57 1 1 0 0 1 1 1V20a1 1 0 0 1-1 1A17 17 0 0 1 3 4a1 1 0 0 1 1-1h3.5a1 1 0 0 1 1 1c0 1.25.2 2.45.57 3.57a1 1 0 0 1-.25 1z"/></svg>(777) 888-7777</p>
    <p class="row"><svg width="4" height="4" viewBox="0 0 24 24"><path d="M2 5h20v14H2z"/></svg>info@yourmail.com</p>
    <p class="row"><svg width="4" height="4" viewBox="0 0 24 24"><circle cx="12" cy="12" r="10"/></svg>www.yourwebsite.com</p>
  </div>
  <svg class="footer-wave" width="183" height="10" viewBox="0 0 183 10" preserveAspectRatio="none">
    <path d="M0 4 Q91 -3 183 4" stroke="var(--rule-grey)" stroke-width="0.8" fill="none"/>
    <path d="M0 6 Q91 1 183 6 V10 H0Z" fill="var(--brand-blue)"/>
  </svg>
</section>

<!-- Business card back -->
<section class="sheet card-back" aria-label="Business card back">
  <div class="brand on-blue">
    <span class="brand-square"></span>
    <span class="brand-name">Lindera<br>Tech</span>
  </div>
</section>

<!-- Envelope back -->
<section class="sheet envelope-back" aria-label="Envelope back">
  <svg class="flap" width="451" height="66" viewBox="0 0 451 66">
    <path d="M0 0 H451 L447 42 Q445 66 418 66 H33 Q6 66 4 42 Z" fill="var(--brand-blue)"/>
  </svg>
  <div class="brand on-blue">
    <span class="brand-square"></span>
    <span class="brand-name">Lindera<br>Tech</span>
  </div>
</section>

<!-- Envelope front -->
<section class="sheet envelope-front" aria-label="Envelope front">
  <div class="brand">
    <span class="brand-square"></span>
    <span class="brand-name">Lindera<br>Tech</span>
  </div>
  <div class="contact">
    <p>1234 First Line Address</p>
    <p>5678 Second Line Address</p>
    <div class="gap"></div>
    <p class="row"><svg width="6" height="6" viewBox="0 0 24 24"><path d="M6.6 10.8a15.1 15.1 0 0 0 6.6 6.6l2.2-2.2a1 1 0 0 1 1-.25 11.4 11.4 0 0 0 3.6.57 1 1 0 0 1 1 1V20a1 1 0 0 1-1 1A17 17 0 0 1 3 4a1 1 0 0 1 1-1h3.5a1 1 0 0 1 1 1c0 1.25.2 2.45.57 3.57a1 1 0 0 1-.25 1z"/></svg>(777) 888-7777</p>
    <p class="row"><svg width="6" height="6" viewBox="0 0 24 24"><path d="M2 5h20v14H2z M3 6l9 7 9-7" stroke="#fff" stroke-width="1.5"/></svg>info@yourmail.com</p>
    <p class="row"><svg width="6" height="6" viewBox="0 0 24 24"><circle cx="12" cy="12" r="10"/><path d="M2 12h20M12 2c3 3 3 17 0 20M12 2c-3 3-3 17 0 20" stroke="#fff" stroke-width="1.3" fill="none"/></svg>www.yourwebsite.com</p>
  </div>
  <svg class="footer-wave" width="451" height="28" viewBox="0 0 451 28" preserveAspectRatio="none">
    <path d="M0 12 Q225 -7 451 12" stroke="var(--rule-grey)" stroke-width="1.6" fill="none"/>
    <path d="M0 17 Q225 1 451 17 V28 H0Z" fill="var(--brand-blue)"/>
  </svg>
</section>

</body>
</html>
```